Building company with a modern and unique product looking for a business card to help us stand out

We currently have a logo but as our business has grown, we feel that our business card is not reflecting our modern and high quality product and help us stand out from the crowd. Our business is mainly in the construction of new homes using a unique method and materials that makes our homes fire proof, vermin and pest resistant and rated to the maximum cyclone category (category 5). We need a business card that helps us stand out as well as communicating professionalism, high quality and trustworthiness. I have attached our current logo with a black and white option, as well as our business card which is double sided. We would like to retain as much of the information that is currently on our business cards, but presented in a more sleek way. We do like our current colour palette ( white, black, yellow and grey) and have been looking primarily at business cards with a black background however we are open to other combinations of colour and layout as long as we stand out. Please feel free to tweak our logo to make it more suitable for a business card, we like the black option that we use but we have had trouble trying to get the white area to match the rest of the logo and blend effectively into a business card. Please do not hesitate to contact us with any questions as we really want this to be successful!

Target Market(s)

Large contracts including government and larger companies

Industry/Entity Type

Business

Contact Information for Business Card

We will be providing this business card to potential clients including key government ministers and large funding companies, our business card should show that we are professional and reliable.

Requirements
Must have
• It must be easy to read and pleasing to the eye, It must contain as much of the information on the current business card and unless something really stands out, we will most likely pick a design that has all of the information included. It must include our logo of course and have some colour included.
Nice to have
• We are looking for a high end business card and would like to see designs that reflect this. We like the gloss/matte contrast, plastic cards with opaque/coloured areas and unique features not seen on everyday paper business cards. It would be nice to see a few different colour combinations, we are open to new ideas so please feel free to take some artistic licence.
Should not have
• Must not be too busy, difficult to read or be distracting from the information conveyed. Other than this please feel free to add your own touches and make it unique!

```html
<!DOCTYPE html>
<html lang="en">
<head>
<meta charset="utf-8">
<title>Stonewell Homes – Business Card</title>
<link href="https://fonts.googleapis.com/css2?family=Marcellus&family=Raleway:wght@400;500&display=swap" rel="stylesheet">
<style>
  :root {
    --page-bg: #d9d4cc;
    --card-black: #121212;
    --card-black-soft: #2a2a2a;
    --frost-light: #f1f1ef;
    --frost-mid: #d8dad9;
    --gold: #c8922c;
    --gold-light: #e0b35a;
    --text-light: #e4e4e4;
    --ink: #1a1a1a;
  }
  * { margin: 0; padding: 0; box-sizing: border-box; }
  html, body {
    width: 1200px; height: 969px; overflow: hidden;
    background: var(--page-bg);
  }
  .canvas { position: relative; width: 1200px; height: 969px; }
  .business-card {
    position: absolute; left: 100px; top: 202px;
    width: 1000px; height: 565px;
    background: linear-gradient(135deg, var(--frost-light) 0%, var(--frost-mid) 100%);
    box-shadow: 0 18px 40px rgba(0,0,0,0.25);
    overflow: hidden;
  }
  .card-shapes { position: absolute; inset: 0; width: 1000px; height: 565px; }
  .contact-panel {
    position: absolute; left: 60px; top: 150px;
    font-family: "Raleway", sans-serif;
    color: var(--text-light);
  }
  .contact-name {
    font-family: "Marcellus", serif;
    font-size: 31px; font-weight: 400; color: var(--gold-light);
    letter-spacing: 0.5px; line-height: 1.1;
  }
  .contact-role { font-size: 24px; margin-top: 6px; letter-spacing: 0.3px; }
  .contact-list { list-style: none; margin-top: 42px; }
  .contact-item {
    display: flex; align-items: center; gap: 18px;
    font-size: 23px; height: 40px; letter-spacing: 0.6px;
  }
  .contact-item.small { font-size: 20px; }
  .contact-icon { width: 24px; height: 24px; flex: none; }
  .brand-mark {
    position: absolute; left: 780px; top: 282px;
    transform: translate(-50%, -50%);
    display: flex; align-items: center; gap: 16px;
    font-family: "Raleway", sans-serif; font-weight: 500;
    font-size: 44px; line-height: 1; letter-spacing: 1px;
    color: var(--ink); white-space: nowrap;
  }
  .brand-square { width: 18px; height: 18px; background: var(--ink); flex: none; }
</style>
</head>
<body>
<div class="canvas">
  <div class="business-card">
    <svg class="card-shapes" viewBox="0 0 1000 565" aria-hidden="true">
      <defs>
        <linearGradient id="darkPanel" x1="0" y1="0" x2="1" y2="1">
          <stop offset="0" stop-color="#2a2a2a"/>
          <stop offset="1" stop-color="#0d0d0d"/>
        </linearGradient>
      </defs>
      <polygon points="0,0 500,0 440,282 560,565 0,565" fill="url(#darkPanel)"/>
      <polyline points="540,0 480,282 600,565" fill="none" stroke="var(--gold)" stroke-width="10"/>
      <polyline points="512,0 452,282 572,565" fill="none" stroke="#ffffff" stroke-opacity="0.5" stroke-width="2"/>
    </svg>

    <div class="contact-panel">
      <h1 class="contact-name">Marcus Fielding</h1>
      <p class="contact-role">Managing Director</p>
      <ul class="contact-list">
        <li class="contact-item">
          <svg class="contact-icon" viewBox="0 0 24 24"><path fill="var(--gold)" d="M6.6 10.8a15 15 0 0 0 6.6 6.6l2.2-2.2c.3-.3.7-.4 1-.2 1.1.4 2.3.6 3.6.6.6 0 1 .4 1 1V20c0 .6-.4 1-1 1A17 17 0 0 1 3 4c0-.6.4-1 1-1h3.5c.6 0 1 .4 1 1 0 1.3.2 2.5.6 3.6.1.3 0 .7-.2 1z"/></svg>
          0400 555 123
        </li>
        <li class="contact-item">
          <svg class="contact-icon" viewBox="0 0 24 24"><rect x="6" y="2" width="12" height="20" rx="2" fill="none" stroke="var(--gold)" stroke-width="2"/><circle cx="12" cy="18" r="1.2" fill="var(--gold)"/></svg>
          (02) 5550 1234
        </li>
        <li class="contact-item small">
          <svg class="contact-icon" viewBox="0 0 24 24"><rect x="2" y="5" width="20" height="14" rx="1.5" fill="var(--gold)"/><polyline points="2.5,6 12,13 21.5,6" fill="none" stroke="#1a1a1a" stroke-width="1.6"/></svg>
          office@stonewellhomes.com
        </li>
        <li class="contact-item small">
          <svg class="contact-icon" viewBox="0 0 24 24"><circle cx="12" cy="12" r="10" fill="var(--gold)"/><path d="M2 12h20M12 2c3 3 3 17 0 20M12 2c-3 3-3 17 0 20" fill="none" stroke="#1a1a1a" stroke-width="1.3"/></svg>
          www.stonewellhomes.com
        </li>
      </ul>
    </div>

    <div class="brand-mark">
      <span class="brand-square"></span>
      <span class="brand-name">Stonewell Homes</span>
    </div>
  </div>
</div>
</body>
</html>
```